Business Card Design

Harlow Sun and Electrical is a new company that specializes in solar pv. I need a card with similar attributes to the ones I have attached. I am after a two sided card with the logo on one side and the logo plus info on the other. I would prefer one side to be black and the other to be a colour but am open to suggestions. The colour scheme I was thinking of was blue or green. I plan on spot glossing the logos if that makes any difference. I have attached a file of my logo in a few colours, none of which I am completely sold on so please feel free to change colous to suit.
Thanks.
Contact Information for Business Card
Dorian Harlow, www.hwx-example.net.nz, dorian@hwx-example.net.nz, t. 0508 4 BRIGHT m. 027469318

```html
<!DOCTYPE html>
<html lang="en">
<head>
<meta charset="utf-8">
<title>Harlow Sun and Electrical — Business Card</title>
<link rel="stylesheet" href="https://fonts.googleapis.com/css2?family=Roboto+Condensed:wght@400;700&display=swap">
<style>
  :root {
    --stage: #1c1c1c;
    --card-white: #fbfbfb;
    --card-white-shade: #eeeeee;
    --card-green: #137a46;
    --card-green-shade: #0f6a3c;
    --brand-green: #0e6e3c;
    --ink-white: #ffffff;
    --ink-dark: #1e2a22;
    --font-main: "Roboto Condensed", "Arial Narrow", sans-serif;
  }
  * { box-sizing: border-box; margin: 0; padding: 0; }
  html, body {
    width: 1200px;
    height: 900px;
    overflow: hidden;
    background: var(--stage);
    font-family: var(--font-main);
  }
  .stage {
    width: 1200px;
    height: 900px;
    display: flex;
    flex-direction: column;
    align-items: center;
    justify-content: center;
    gap: 56px;
  }
  .card {
    position: relative;
    width: 640px;
    height: 366px;
    overflow: hidden;
    box-shadow: 0 10px 30px rgba(0, 0, 0, 0.45);
  }
  .card--front { background: var(--card-white); }
  .card--back { background: var(--card-green); }

  .card__texture {
    position: absolute;
    inset: 0;
  }
  .card--front .card__texture {
    background: linear-gradient(120deg, var(--card-white) 45%, var(--card-white-shade) 100%);
  }
  .card--back .card__texture {
    background: linear-gradient(135deg, var(--card-green-shade) 0%, var(--card-green) 60%, var(--card-green-shade) 100%);
  }

  .wordmark {
    position: absolute;
    display: flex;
    align-items: center;
    gap: 12px;
    font-weight: 700;
    text-transform: uppercase;
    letter-spacing: 0.02em;
    white-space: nowrap;
  }
  .wordmark__dot {
    width: 22px;
    height: 22px;
    border-radius: 50%;
    flex: none;
  }
  .card--front .wordmark {
    left: 120px;
    top: 92px;
    font-size: 30px;
    color: var(--brand-green);
  }
  .card--front .wordmark__dot { background: var(--brand-green); }
  .card--back .wordmark {
    right: 44px;
    bottom: 96px;
    font-size: 30px;
    color: var(--ink-white);
  }
  .card--back .wordmark__dot { background: var(--ink-white); }

  .contact-name {
    position: absolute;
    left: 120px;
    top: 190px;
    font-size: 26px;
    font-weight: 700;
    text-transform: uppercase;
    color: var(--brand-green);
  }
  .contact-list {
    position: absolute;
    list-style: none;
    font-size: 15px;
    line-height: 1.4;
    text-transform: uppercase;
    color: var(--ink-dark);
  }
  .contact-list--phones { left: 120px; top: 236px; }
  .contact-list--online { left: 370px; top: 186px; }
  .contact-list .label { color: var(--brand-green); margin-right: 4px; }
  .contact-list .web { color: var(--brand-green); }
</style>
</head>
<body>
  <main class="stage">
    <section class="card card--front" aria-label="Business card, front">
      <div class="card__texture" role="img" aria-label="Faint light grey repeating brand pattern across the card"></div>
      <div class="wordmark">
        <span class="wordmark__dot" aria-hidden="true"></span>
        <span class="wordmark__name">Harlow Sun &amp; Electrical</span>
      </div>
      <h1 class="contact-name">Dorian Harlow</h1>
      <ul class="contact-list contact-list--phones">
        <li><span class="label">M:</span>027469318</li>
        <li><span class="label">T:</span>0508 4 BRIGHT (274448)</li>
      </ul>
      <ul class="contact-list contact-list--online">
        <li><span class="label">E:</span>dorian@hwx-example.net.nz</li>
        <li class="web">www.hwx-example.net.nz</li>
      </ul>
    </section>

    <section class="card card--back" aria-label="Business card, back">
      <div class="card__texture" role="img" aria-label="Green field with a faint darker repeating brand pattern"></div>
      <div class="wordmark">
        <span class="wordmark__dot" aria-hidden="true"></span>
        <span class="wordmark__name">Harlow Sun &amp; Electrical</span>
      </div>
    </section>
  </main>
</body>
</html>
```